Party Favors and Decorations Business Needs A Business Card Design

We are in need of a Logo design and business card design for a new small business called Willow Bay Designs. We create party decorations and favours for Bridal Showers, Baby Showers, Weddings Birthdays etc. This is a very personalized service based on Clients theme, colour, and style. We are looking for a high end elegant look. I have attached a file to the style I like including the type of paper.

Target Market(s)

women, young adults, expectant mothers, mothers

Industry/Entity Type

Small Business

Contact Information for Business Card

Willow Bay Designs Essex, ON 519-806-4192 willowbaydesigns-example.ca danielle@willowbaygiftwrap-example.com find us on Friendlink

Logo Text

Willow Bay Designs

Font styles to use
Script

Requirements
Must have
• Name, email, web address, phone number
Should not have
• cutesy graphics

```html
<!DOCTYPE html>
<html lang="en">
<head>
<meta charset="utf-8">
<title>Willow Bay Designs — Business Card</title>
<link rel="stylesheet" href="https://fonts.googleapis.com/css2?family=Playfair+Display+SC:wght@400;700&family=Pinyon+Script&display=swap">
<style>
  :root {
    --crimson: #c70f33;
    --wine: #8e1330;
    --maroon: #4e0f22;
    --ink: #0b0507;
    --cream: #fbf6f2;
    --glow: rgba(255, 190, 200, 0.22);
  }
  html, body {
    margin: 0;
    padding: 0;
    overflow: hidden;
    background: var(--maroon);
  }
  .card {
    position: relative;
    width: 1200px;
    height: 686px;
    overflow: hidden;
    background:
      radial-gradient(circle at 78% 22%, var(--glow) 0, transparent 38%),
      radial-gradient(circle at 60% 85%, var(--glow) 0, transparent 32%),
      radial-gradient(circle at 30% 70%, rgba(255,190,200,0.14) 0, transparent 30%),
      linear-gradient(120deg, var(--crimson) 0%, var(--wine) 50%, var(--maroon) 100%);
    font-family: "Playfair Display SC", "Times New Roman", serif;
    color: var(--cream);
  }
  .balloons-illustration {
    position: absolute;
    left: 46px;
    top: 16px;
    width: 330px;
    height: 320px;
    border-radius: 140px 140px 60px 60px;
    background: linear-gradient(180deg, rgba(11,5,7,0.85) 0%, rgba(11,5,7,0.6) 100%);
  }
  .glass-illustration {
    position: absolute;
    left: 52px;
    top: 362px;
    width: 86px;
    height: 300px;
    border-radius: 8px 8px 30px 30px;
    background: linear-gradient(180deg, rgba(60,8,22,0.85) 0%, rgba(11,5,7,0.85) 100%);
  }
  .brand-name {
    position: absolute;
    left: 200px;
    top: 96px;
    margin: 0;
    font-size: 80px;
    font-weight: 700;
    letter-spacing: 2px;
    line-height: 1;
    white-space: nowrap;
  }
  .tagline {
    position: absolute;
    left: 0;
    width: 1170px;
    top: 214px;
    margin: 0;
    text-align: center;
    font-size: 44px;
    font-weight: 700;
    line-height: 58px;
    letter-spacing: 1px;
  }
  .occasions {
    position: absolute;
    left: 0;
    width: 1160px;
    top: 358px;
    margin: 0;
    padding: 0;
    list-style: none;
    text-align: center;
    font-size: 62px;
    font-weight: 700;
    line-height: 88px;
    letter-spacing: 2px;
    white-space: nowrap;
  }
  .swash {
    font-family: "Pinyon Script", cursive;
    font-weight: 400;
    font-size: 1.4em;
    line-height: 0;
    letter-spacing: 0;
  }
  .contact {
    position: absolute;
    left: 160px;
    right: 30px;
    top: 640px;
    margin: 0;
    text-align: center;
    font-size: 19px;
    font-weight: 400;
    letter-spacing: 0.5px;
    white-space: nowrap;
  }
  .contact span + span::before {
    content: "·";
    margin: 0 12px;
  }
</style>
</head>
<body>
  <main class="card">
    <div class="balloons-illustration" role="img" aria-label="Illustration of three black balloons with strings"></div>
    <div class="glass-illustration" role="img" aria-label="Illustration of a champagne flute filled with red wine"></div>

    <h1 class="brand-name">Willow Bay Designs</h1>

    <p class="tagline"><span class="swash">W</span>e create party<br>decorations &amp; favours for</p>

    <ul class="occasions">
      <li><span class="swash">B</span>ridal <span class="swash">S</span>howers</li>
      <li><span class="swash">B</span>aby <span class="swash">S</span>howers</li>
      <li><span class="swash">W</span>eddings <span class="swash">B</span>irthdays</li>
    </ul>

    <p class="contact"><span>519-806-4192</span><span>willowbaydesigns-example.ca</span><span>danielle@willowbaygiftwrap-example.com</span></p>
  </main>
</body>
</html>
```